New one page Homepage with registration and log in form

Hi designers!

We need a new homepage and made a skitch of how it should be.

Can you give some of your design ideas and work it out so that it actually looks great?

Its just one page, for convertion reasons.

The logo doesnt have to be changed.

It would be cool to center the logo but not sure how design technically correct that is.

The social icons can be left out.

If you could give a few mockups than we can choose the best one.

I added one screenshot sketch of the homepage.

And 2 screenshots of what the system looks like on the inside, just so you get an idea.

Thanks

Target Market(s)

Vacation rental owners who want to increase their bookings by connecting with other VR owners and managers, or by having their own booking team for a small fee.

Industry/Entity Type

Social

Number of Pages Required

1 page

Requirements
Must have
• Use your imagination please
Nice to have
• Use your imagination
• It will be a one page design so we need to impress :)
• Keep it compact, maybe a web 3.0 flat design, etc
Should not have
• Other pages.

```html
<!DOCTYPE html>
<html lang="en">
<head>
<meta charset="utf-8">
<title>StayCircle – The First Social Booking Network</title>
<link href="https://fonts.googleapis.com/css2?family=Lato:wght@400;700&display=swap" rel="stylesheet">
<style>
:root{
  --page:#f1f1f1;
  --header:#f8f8f8;
  --card:#ffffff;
  --line:#dcdcdc;
  --text:#333333;
  --muted:#666666;
  --brand:#1b4f9c;
  --orange-top:#ffad00;
  --orange-bot:#ff8a00;
  --green-top:#1fb555;
  --green-bot:#169c43;
  --blue-btn:#0d49ad;
  --player:#1c4fa7;
  --social-a:#3b5998;
  --social-b:#3fa9e0;
  --social-c:#d8392b;
}
*{box-sizing:border-box;margin:0;padding:0}
html,body{width:1200px;height:1171px;overflow:hidden}
body{background:var(--page);font-family:"Lato",sans-serif;color:var(--text);font-size:13px}
.wrap{width:980px;margin:0 auto;position:relative}

.site-header{height:97px;background:var(--header);border-bottom:1px solid var(--line)}
.site-header .wrap{height:97px}
.brand{position:absolute;left:2px;top:16px;display:flex;align-items:center;gap:10px}
.brand-square{width:34px;height:34px;background:var(--brand);border-radius:4px}
.brand-name{font-size:26px;font-weight:700;color:var(--brand)}
.follow{position:absolute;right:0;top:10px;display:flex;align-items:center;gap:8px;font-size:13px;color:var(--muted)}
.dot{width:26px;height:26px;border-radius:50%}
.dot.a{background:var(--social-a)}.dot.b{background:var(--social-b)}.dot.c{background:var(--social-c)}
.login-toggle{position:absolute;right:0;top:53px;width:88px;height:30px;border:1px solid var(--line);border-radius:3px;background:#fff;display:flex;align-items:center;justify-content:center;gap:7px;font-size:13px;color:var(--muted)}

.hero{height:404px;border-bottom:1px solid var(--line);position:relative}
.hero h1{text-align:center;font-size:27px;font-weight:700;padding-top:26px;height:81px;color:#222}
.video{position:absolute;left:0;top:81px;width:493px;height:297px;background:var(--card);border:1px solid #e4e4e4;border-radius:3px}
.video .big-play{position:absolute;left:185px;top:72px}
.controls{position:absolute;left:11px;top:254px;width:470px;height:26px;display:flex}
.controls .btn{width:37px;background:var(--player);display:flex;align-items:center;justify-content:center}
.controls .track{flex:1;background:#666;position:relative}
.controls .track span{position:absolute;left:10px;right:12px;top:8px;height:9px;background:#fff}
.controls .track i{position:absolute;left:10px;width:46px;top:8px;height:9px;background:#aaa}
.intro{position:absolute;left:513px;top:74px;width:467px;font-size:14px;line-height:23px;color:#333}
.intro p{margin-bottom:23px}

.accounts{height:501px;border-top:1px solid #fff;position:relative}
.card{position:absolute;top:28px;height:452px;background:var(--card);border:1px solid #e4e4e4;border-radius:3px}
.card h2{text-align:center;font-size:22px;font-weight:400;color:#333}
.login{left:0;width:493px}
.login h2{margin-top:24px}
.register{left:509px;width:471px}
.register h2{margin-top:24px}
.sub{text-align:center;font-size:11px;color:var(--muted);margin-top:3px}
.field{height:37px;border:1px solid #ccc;border-radius:3px;background:#fff;font-size:13px;color:#555;display:flex;align-items:center;padding-left:17px;font-family:inherit}
.login .field{position:absolute;left:32px;width:430px}
.f1{top:78px}.f2{top:130px}
.remember{position:absolute;left:32px;top:182px;display:flex;align-items:center;gap:11px;font-size:13px}
.remember .box{width:24px;height:24px;border:1px solid #ccc;border-radius:3px}
.btn-login{position:absolute;left:32px;top:216px;width:430px;height:51px;border-radius:3px;background:linear-gradient(var(--orange-top),var(--orange-bot));color:#fff;font-size:18px;font-weight:700;display:flex;align-items:center;justify-content:center}
.social-label{position:absolute;left:0;right:0;top:312px;text-align:center;font-size:12px;font-weight:700}
.btn-social{position:absolute;left:133px;top:342px;width:228px;height:42px;border-radius:3px;background:var(--blue-btn);color:#fff;font-size:12px;display:flex;align-items:center;padding-left:19px;gap:21px}
.btn-social .sq{width:10px;height:16px;background:#fff;border-radius:2px}
.forgot{position:absolute;left:0;right:0;top:398px;text-align:center;font-size:12px;color:#888}
.reg-form{position:absolute;left:22px;top:80px;width:429px}
.reg-form .row{display:flex;gap:12px;margin-bottom:12px}
.reg-form .field{margin-bottom:12px}
.reg-form .row .field{flex:1;margin-bottom:0}
.btn-register{position:absolute;left:24px;top:369px;width:430px;height:52px;border-radius:3px;background:linear-gradient(var(--green-top),var(--green-bot));color:#fff;font-size:18px;font-weight:700;display:flex;align-items:center;justify-content:center}

.site-footer{height:133px;border-top:1px solid var(--line);background:var(--header)}
.site-footer .wrap{display:flex;padding-top:13px}
.col h3{font-size:14px;font-weight:700;color:#333;margin-bottom:9px}
.col a{display:block;font-size:11px;color:#444;text-decoration:none;line-height:20.5px}
.col.first{width:186px}.col.c2{width:193px}.col.c3{width:241px}.col.c4{width:160px}
.col .spacer{height:26px}
.col .icons{display:flex;gap:8px}
.copyright{height:37px;border-top:1px solid #ddd;background:var(--page);text-align:center;font-size:11px;color:#444;line-height:36px}
</style>
</head>
<body>
<header class="site-header">
  <div class="wrap">
    <div class="brand"><div class="brand-square"></div><span class="brand-name">StayCircle</span></div>
    <div class="follow">Follow Us <span class="dot a"></span><span class="dot b"></span><span class="dot c"></span></div>
    <div class="login-toggle">
      <svg width="11" height="12" viewBox="0 0 11 12"><circle cx="5.5" cy="3.5" r="3" fill="#777"/><path d="M0 12c0-4 2.5-5 5.5-5s5.5 1 5.5 5z" fill="#777"/></svg>
      Login
      <svg width="9" height="6" viewBox="0 0 9 6"><path d="M0 0h9L4.5 6z" fill="#888"/></svg>
    </div>
  </div>
</header>

<section class="hero">
  <div class="wrap">
    <h1>The First Social Booking Network</h1>
    <div class="video">
      <svg class="big-play" width="124" height="124" viewBox="0 0 124 124"><circle cx="62" cy="62" r="56" fill="none" stroke="#c8c8c8" stroke-width="9"/><path d="M48 40v44l38-22z" fill="#c8c8c8"/></svg>
      <div class="controls">
        <div class="btn"><svg width="12" height="14" viewBox="0 0 12 14"><path d="M0 0v14l12-7z" fill="#fff"/></svg></div>
        <div class="track"><span></span><i></i></div>
        <div class="btn"><svg width="18" height="14" viewBox="0 0 18 14"><rect x="1" y="1" width="16" height="12" fill="none" stroke="#fff" stroke-width="1.5"/><path d="M6 5l6 5M12 6v4H8" fill="none" stroke="#fff" stroke-width="1.5"/></svg></div>
      </div>
    </div>
    <div class="intro">
      <p>StayCircle is a new Social Booking Network.<br>Vacation Rental hosts and property Managers can find&nbsp; each other<br>connect and chat amongst themselves for sharing reservation<br>inquiries, services or anything you can imagine, in a convenient social<br>enviorement.</p>
      <p>The Social Booking Network is absolutely FREE. Howeaver if you want to save time and get really professional about increasing your bookingss. Than you should consider having your own Booking Team.</p>
      <p>For just 2.5% your own StayCircle crew take care of all tedious online reservation management tasks for ou in the most advanced, personalized and professional way possible.</p>
    </div>
  </div>
</section>

<section class="accounts">
  <div class="wrap">
    <div class="card login">
      <h2>Login to your account</h2>
      <div class="field f1">Your username or email address</div>
      <div class="field f2">Your password</div>
      <div class="remember"><span class="box"></span>Would you like us to remember you?</div>
      <div class="btn-login">LOG ME IN</div>
      <div class="social-label">Sign in with your social identity</div>
      <div class="btn-social"><span class="sq"></span>Sign in with Circlebook</div>
      <div class="forgot">I forget my username / password</div>
    </div>
    <div class="card register">
      <h2>Don’t have an account</h2>
      <div class="sub">Register now to join the Free Booking Network!</div>
      <div class="reg-form">
        <div class="row"><div class="field">First Name</div><div class="field">Last Name</div></div>
        <div class="field">Username</div>
        <div class="field">Password</div>
        <div class="field">user@mailbox.net</div>
        <div class="field">Your Contact Number Ex. +15550123456</div>
        <div class="field">Whats your reason for joining?</div>
      </div>
      <div class="btn-register">REGISTER</div>
    </div>
  </div>
</section>

<footer class="site-footer">
  <div class="wrap">
    <div class="col first"><h3>ABOUT US</h3><a href="#">Home</a><a href="#">About Us</a><a href="#">Contact</a><a href="#">Circle Book</a></div>
    <div class="col c2"><div class="spacer"></div><a href="#">Calendar</a><a href="#">Properties</a><a href="#">Contact Us</a></div>
    <div class="col c3"><div class="spacer"></div><a href="#">Disclaimer</a><a href="#">Sitemap</a><a href="#">Privacy Policy</a></div>
    <div class="col c4"><div class="spacer"></div><a href="#">Automations</a><a href="#">Channels</a><a href="#">Tools</a></div>
    <div class="col"><h3>FOLLOW US</h3><div class="icons"><span class="dot a"></span><span class="dot b"></span><span class="dot c"></span></div></div>
  </div>
</footer>
<div class="copyright">Copyright © 2014 staycircle.net. All Rights Reserved.</div>
</body>
</html>
```